Plumbing Business - Service Vehicle Wrap

Hi,
We would like assistance to redesign our current vehicle wrap design.
We are happy with the current design & placement of wording etc.
We are not happy with the amount of blue towards the front of the vehicle (mostly the cab)
We would like the front of the vehicle to be white and somehow transition from white into the blue design for the tray and service body.
I have attached a photo of our previous, very simple vehicle signage - we would like to new design to be somewhere between the old design and new.
Keep in simple and clean - Less is more..
Target Market(s)
Commercial
Industry/Entity Type
Plumbing
Other font styles liked:
- As per photo attachments
Look and feel
Each slider illustrates characteristics of the customer's brand and the style your logo design should communicate.

```html
<!DOCTYPE html>
<html lang="en">
<head>
<meta charset="utf-8">
<title>Kestrel Plumbing – Vehicle Wrap Artwork</title>
<link href="https://fonts.googleapis.com/css2?family=Poppins:wght@300;400;700;800&display=swap" rel="stylesheet">
<style>
  :root{
    --page:#f3f4f6;
    --blue-deep:#0a4a98;
    --blue-mid:#0862b0;
    --blue-bright:#0a7cc6;
    --blue-soft:#7fb2e2;
    --white:#ffffff;
    --ink:#2b2b30;
    --grey:#8a8d94;
    --panel-edge:#c9ccd2;
  }
  *{box-sizing:border-box;margin:0;padding:0}
  html,body{width:1200px;height:1200px;overflow:hidden;background:var(--page);font-family:"Poppins",sans-serif}
  .artboard{position:relative;width:1200px;height:1200px}

  /* Service body side panel */
  .service-body{position:absolute;left:60px;top:150px;width:1080px;height:380px;
    background:linear-gradient(100deg,var(--blue-deep) 0%,var(--blue-mid) 55%,var(--blue-bright) 100%);
    overflow:hidden;box-shadow:0 0 0 10px var(--panel-edge)}
  .service-body .wave{position:absolute;inset:0;width:100%;height:100%}
  .service-body .frame{position:absolute;left:22px;top:16px;right:22px;bottom:16px;border:1px solid rgba(0,30,80,.45)}
  .tel{position:absolute;left:60px;top:34px;font-weight:800;font-size:40px;color:var(--white);letter-spacing:-.5px}
  .tel .label{color:var(--blue-soft)}
  .brand-name{position:absolute;left:56px;top:72px;font-weight:300;font-size:150px;line-height:1;color:var(--white);letter-spacing:2px}
  .brand-dot{position:absolute;left:352px;top:250px;width:34px;height:34px;border-radius:50%;background:#4fb4ea}
  .web{position:absolute;left:66px;top:308px;font-weight:400;font-size:24px;color:var(--white);letter-spacing:1px}

  .services{position:absolute;right:44px;top:44px;list-style:none;display:flex;flex-direction:column;gap:22px}
  .service{display:flex;align-items:center;justify-content:flex-end;gap:14px}
  .service span{font-weight:700;font-size:15px;line-height:1.15;color:var(--white);text-align:right;text-transform:uppercase}
  .service svg{width:46px;height:46px;flex:none}

  /* Cab door decal */
  .cab-door{position:absolute;left:340px;top:640px;width:520px;height:400px;background:var(--white);
    border:2px solid var(--panel-edge);border-radius:14px 60px 14px 14px}
  .door-name{position:absolute;left:0;right:0;top:130px;text-align:center;font-weight:300;font-size:96px;line-height:1;color:var(--ink);letter-spacing:1px}
  .door-tag{position:absolute;left:0;right:0;top:262px;text-align:center;font-weight:300;font-size:12px;color:var(--grey);letter-spacing:11px}
</style>
</head>
<body>
<main class="artboard">

  <section class="service-body" aria-label="Service body side panel">
    <svg class="wave" viewBox="0 0 1080 380" preserveAspectRatio="none" aria-hidden="true">
      <path d="M0 0H1080V150H0Z" fill="rgba(255,255,255,.04)"/>
      <path d="M0 220 C300 270 700 300 1080 140 V380 H0Z" fill="rgba(10,90,175,.55)"/>
      <path d="M0 150H1080" stroke="rgba(0,40,110,.25)" stroke-width="60"/>
    </svg>
    <div class="frame"></div>

    <p class="tel"><span class="label">TEL:</span> 1300 468 902</p>
    <h1 class="brand-name">kestrel</h1>
    <span class="brand-dot"></span>
    <p class="web">kestrelplumbing.com.au</p>

    <ul class="services">
      <li class="service"><span>Service &amp;<br>Maintenance</span>
        <svg viewBox="0 0 46 46"><circle cx="23" cy="23" r="21" fill="none" stroke="#fff" stroke-width="2"/><path d="M15 31 L31 15 M15 15 L31 31" stroke="#0b5cb0" stroke-width="3"/></svg></li>
      <li class="service"><span>Projects &amp;<br>Installation</span>
        <svg viewBox="0 0 46 46"><circle cx="23" cy="23" r="21" fill="none" stroke="#fff" stroke-width="2"/><rect x="14" y="15" width="18" height="16" fill="none" stroke="#0b5cb0" stroke-width="2"/></svg></li>
      <li class="service"><span>Strata &amp;<br>Real Estate</span>
        <svg viewBox="0 0 46 46"><circle cx="23" cy="23" r="21" fill="none" stroke="#fff" stroke-width="2"/><rect x="17" y="12" width="12" height="22" fill="none" stroke="#0b5cb0" stroke-width="2"/></svg></li>
      <li class="service"><span>24/7 Emergency<br>Response</span>
        <svg viewBox="0 0 46 46"><circle cx="23" cy="23" r="21" fill="none" stroke="#fff" stroke-width="2"/><path d="M15 31 L31 15" stroke="#0b5cb0" stroke-width="3"/></svg></li>
    </ul>
  </section>

  <section class="cab-door" aria-label="Cab door decal">
    <h2 class="door-name">kestrel</h2>
    <p class="door-tag">plumbing services</p>
  </section>

</main>
</body>
</html>
```